Boutique Fitness Facility needs a new meal plan design that is as hot as our workouts!

We are about to host our 6 week Coral Tide program and we need to have a great looking meal plan handout created that we can give to all of our participants.

I have attached an example of our current full meal plan, for a reference only.

As in the example I've provided, I'd like to have certain areas color coded such as the proteins being Blue, Fats -yellow, Carbs - orange and veggies- green.

These colors will corollate to the Breakfast - snack - lunch - snack - Dinner graph that I've provided and would like to have added to the new handout.

I would like our logo placed at the top and beneath the logo have the text "Coral Tide Challenge"

The flyer should be of a summer influence in colors and design and
All text should be easy to read.

Thank you and I look forward to seeing your design!

```html
<!DOCTYPE html>
<html lang="en">
<head>
<meta charset="utf-8">
<title>PulseForge – Coral Tide Challenge Meal Plan</title>
<link href="https://fonts.googleapis.com/css2?family=Inter+Tight:wght@400;500;700;800;900&display=swap" rel="stylesheet">
<style>
:root{
  --ink:#111111;
  --white:#ffffff;
  --protein:#3b53a8;
  --fats:#f5c800;
  --carbs:#f7901e;
  --veggies:#5cb946;
  --sun-orange:#ff8a1a;
  --coral:#f4a29a;
  --lagoon:#1fd8ef;
  --lemon:#ffd21a;
  --text:#3a3a3a;
}
*{box-sizing:border-box;margin:0;padding:0}
html,body{width:908px;height:1200px;overflow:hidden;background:var(--white)}
body{font-family:"Inter Tight",Arial,sans-serif;color:var(--ink)}
.flyer{position:relative;width:908px;height:1200px;overflow:hidden;
  background:
    linear-gradient(180deg,rgba(255,210,26,0) 55%,rgba(255,210,26,.9) 100%),
    linear-gradient(100deg,var(--sun-orange) 0%,#ff9a3a 30%,var(--coral) 55%,#b9c6e6 72%,var(--lagoon) 100%);}
.header-band{position:absolute;left:0;top:0;width:908px;height:380px}
.dumbbell{position:absolute;background:linear-gradient(135deg,#ffd84a,#e8a800);border-radius:40px}
.dumbbell.left{left:34px;top:58px;width:150px;height:52px;transform:rotate(-48deg)}
.dumbbell.right{left:690px;top:240px;width:150px;height:52px;transform:rotate(58deg)}
.brand{position:absolute;left:0;width:908px;top:46px;text-align:center;font-weight:900;font-size:108px;line-height:1;color:var(--white);letter-spacing:-4px;text-transform:none}
.tagline{position:absolute;left:0;width:908px;top:180px;text-align:center;font-weight:800;font-size:15px;letter-spacing:5px;color:var(--fats)}
.challenge{position:absolute;left:223px;top:214px;width:499px;height:48px;background:var(--fats);border:3px solid var(--white);text-align:center;font-weight:900;font-size:29px;line-height:42px;letter-spacing:-1.2px;text-transform:uppercase}
.column{position:absolute;top:281px;width:198px;height:403px;background:var(--white);border:2px solid}
.column h2{height:42px;margin:-2px -2px 0;padding-left:12px;font-size:16px;font-weight:700;line-height:42px;color:var(--white);letter-spacing:-.2px}
.column ul{list-style:none;padding:18px 8px 0 12px}
.column li{position:relative;padding-left:24px;font-size:11px;line-height:13px;color:var(--text);margin-bottom:14px;letter-spacing:-.2px}
.column li::before{content:"";position:absolute;left:2px;top:2px;width:9px;height:9px;border-radius:50%;background:var(--dot)}
.column .intro{padding-left:0;margin-bottom:12px}
.column .intro::before{display:none}
.protein{left:36px;border-color:var(--protein);--dot:var(--protein)}
.protein h2{background:var(--protein)}
.protein li{margin-bottom:8px}
.fats{left:248px;border-color:var(--fats);--dot:var(--fats)}
.fats h2{background:var(--fats)}
.carbs{left:460px;border-color:var(--carbs);--dot:var(--carbs)}
.carbs h2{background:var(--carbs)}
.veggies{left:671px;border-color:var(--veggies);--dot:var(--veggies)}
.veggies h2{background:var(--veggies)}
.meal-ring{position:absolute;top:704px;width:176px;height:176px}
.meal-ring span{position:absolute;inset:0;display:flex;align-items:center;justify-content:center;font-weight:700;font-size:18px;letter-spacing:-.4px}
.snack{position:absolute;top:762px;width:98px;text-align:center;color:var(--white)}
.snack svg{display:block;margin:0 auto 8px}
.snack b{display:block;background:var(--ink);font-size:17px;font-weight:700;line-height:28px;letter-spacing:-.4px}
.snack p{margin-top:8px;font-size:17px;line-height:17px;letter-spacing:-.6px}
.portrait{position:absolute;left:300px;top:820px;width:330px;height:380px;border-radius:150px 150px 0 0;background:linear-gradient(180deg,#c8906d 0%,#e8c0a6 45%,#cfcfd2 75%,#bdbdc2 100%)}
.supplements{position:absolute;left:37px;top:914px;width:300px;height:247px;background:var(--lemon);border:3px solid var(--white);border-right:none;padding:30px 0 0 26px}
.supplements h3{font-size:24px;font-weight:900;letter-spacing:-.8px;margin-bottom:10px}
.supplements p{font-size:21px;line-height:27px;letter-spacing:-.8px;width:260px}
.supplements strong{font-weight:800}
.stack{position:absolute;left:636px;color:var(--ink)}
.stack svg{position:absolute;left:0;top:0}
.stack h3{margin-left:41px;font-size:24px;font-weight:900;letter-spacing:-1px;line-height:28px}
.stack p{margin-left:41px;font-size:22px;line-height:27px;letter-spacing:-.8px;margin-top:4px}
.stack.am{top:920px}
.stack.pm{top:1054px}
</style>
</head>
<body>
<main class="flyer">
  <svg class="header-band" viewBox="0 0 908 380" aria-hidden="true">
    <path d="M0 0H908V292C700 318 320 340 0 366Z" fill="#121212"/>
  </svg>
  <div class="dumbbell left" role="img" aria-label="Yellow dumbbell"></div>
  <div class="dumbbell right" role="img" aria-label="Yellow dumbbell"></div>

  <h1 class="brand">PulseForge</h1>
  <p class="tagline">PERSONAL GROUP TRAINING</p>
  <div class="challenge">Coral Tide Challenge</div>

  <section class="column protein">
    <h2>P-Protein (PALM)</h2>
    <ul>
      <li>6oz. Chicken Breast (Skinless)</li>
      <li>6oz. Bison Burger</li>
      <li>6oz. Venison</li>
      <li>6oz. 99% Lean Turkey Breast</li>
      <li>6oz. Pork Tenderloin</li>
      <li>6oz. 96/4 Ground Beef</li>
      <li>6oz. Any White Fish</li>
      <li>6oz. Any Shellfish</li>
      <li>1.25 Cup Egg Whites</li>
      <li>6 Egg Whites</li>
      <li>1.5 Cup 0% Cottage Cheese</li>
      <li>1.5 Cup 0% Greek Yogurt</li>
      <li>1.5 Scoop Protein Powder</li>
      <li>1.5 Cans Tuna</li>
    </ul>
  </section>

  <section class="column fats">
    <h2>F-Fats (TB)</h2>
    <ul>
      <li>2TB. Peanut</li>
      <li>2TB. Almond Butter</li>
      <li>1.5TB. Coconut Butter</li>
      <li>2TB. Grassfed Butter</li>
      <li>1.5TB. Olive Oil</li>
      <li>1/2 of Medium Avocado</li>
      <li>0.25 Cup Any Nuts</li>
      <li>4 TB. Coffee Creamer</li>
      <li>1.5TB. Any Cooking Oil</li>
      <li>Not Vegitable Oil</li>
      <li>Not Canola Oil</li>
    </ul>
  </section>

  <section class="column carbs">
    <h2>C-Carbs (FIST)</h2>
    <ul>
      <li>.75 Cup Mash Sweet Potato</li>
      <li>.75 Cup Mash Red Potato</li>
      <li>.5 Cup Any Bean/Legume</li>
      <li>.5 Cup Cooked Brown Rice</li>
      <li>.5 Cup Cooked White Rice</li>
      <li>1.5 Slices Ezekiel Bread</li>
      <li>.5 Cup (Dry) Rolled Oats</li>
      <li>.5 Cup Pasta</li>
      <li>.75 Cup Any Berries</li>
      <li>.5 Cup Cooked Quino</li>
    </ul>
  </section>

  <section class="column veggies">
    <h2>V-Veggies (FIST)</h2>
    <ul>
      <li class="intro">Any Veggie Except:</li>
      <li>Peas</li>
      <li>Carrots</li>
      <li>Corn</li>
      <li>Any Type of Squash</li>
      <li>Eggplant</li>
      <li>Pumpkin</li>
      <li>Beets</li>
      <li>Stick W Green &amp;</li>
      <li>Leafy Veggies</li>
    </ul>
  </section>

  <div class="portrait" role="img" aria-label="Photo of a fit woman in a grey tank top"></div>

  <div class="meal-ring" style="left:41px">
    <svg viewBox="0 0 176 176" width="176" height="176" aria-hidden="true">
      <circle cx="88" cy="88" r="80" fill="var(--white)"/>
      <circle cx="88" cy="88" r="76" fill="none" stroke="var(--carbs)" stroke-width="16"/>
      <circle cx="88" cy="88" r="76" fill="none" stroke="var(--protein)" stroke-width="16" stroke-dasharray="160 318" transform="rotate(-92 88 88)"/>
      <circle cx="88" cy="88" r="76" fill="none" stroke="var(--veggies)" stroke-width="16" stroke-dasharray="150 328" transform="rotate(36 88 88)"/>
    </svg>
    <span>Breakfast</span>
  </div>
  <div class="meal-ring" style="left:357px">
    <svg viewBox="0 0 176 176" width="176" height="176" aria-hidden="true">
      <circle cx="88" cy="88" r="80" fill="var(--white)"/>
      <circle cx="88" cy="88" r="76" fill="none" stroke="var(--carbs)" stroke-width="16"/>
      <circle cx="88" cy="88" r="76" fill="none" stroke="var(--protein)" stroke-width="16" stroke-dasharray="160 318" transform="rotate(-92 88 88)"/>
      <circle cx="88" cy="88" r="76" fill="none" stroke="var(--veggies)" stroke-width="16" stroke-dasharray="150 328" transform="rotate(36 88 88)"/>
    </svg>
    <span>Lunch</span>
  </div>
  <div class="meal-ring" style="left:687px">
    <svg viewBox="0 0 176 176" width="176" height="176" aria-hidden="true">
      <circle cx="88" cy="88" r="80" fill="var(--white)"/>
      <circle cx="88" cy="88" r="76" fill="none" stroke="var(--carbs)" stroke-width="16"/>
      <circle cx="88" cy="88" r="76" fill="none" stroke="var(--protein)" stroke-width="16" stroke-dasharray="160 318" transform="rotate(-92 88 88)"/>
      <circle cx="88" cy="88" r="76" fill="none" stroke="var(--veggies)" stroke-width="16" stroke-dasharray="150 328" transform="rotate(36 88 88)"/>
    </svg>
    <span>Dinner</span>
  </div>

  <div class="snack" style="left:238px;top:730px">
    <svg width="44" height="22" viewBox="0 0 44 22" aria-hidden="true"><path d="M2 11H40M31 2L41 11L31 20" stroke="var(--white)" stroke-width="2.5" fill="none"/></svg>
    <b>Snack</b>
    <p>1/2 Portion<br>of Protein</p>
  </div>
  <div class="snack" style="left:540px;top:730px">
    <svg width="44" height="22" viewBox="0 0 44 22" aria-hidden="true"><path d="M2 11H40M31 2L41 11L31 20" stroke="var(--white)" stroke-width="2.5" fill="none"/></svg>
    <b>Snack</b>
    <p>1/2 Portion<br>of Protein</p>
  </div>

  <section class="supplements">
    <h3>SUPPLEMENTS</h3>
    <p><strong>Pro Tip:</strong> Keep your supps next to things you use every AM and PM. Ex: car keys, toothbrush</p>
  </section>

  <section class="stack am">
    <svg width="40" height="40" viewBox="0 0 40 40" aria-hidden="true">
      <g stroke="#ff9d1a" stroke-width="3" stroke-linecap="round">
        <path d="M20 2v6M20 32v6M2 20h6M32 20h6M7 7l4 4M29 29l4 4M7 33l4-4M29 11l4-4"/>
      </g>
      <circle cx="20" cy="20" r="9" fill="#ffd21a"/>
    </svg>
    <h3>AM STACK</h3>
    <p>Multi-Vital<br>Ignite AM<br>Drive Stack</p>
  </section>

  <section class="stack pm">
    <svg width="36" height="36" viewBox="0 0 36 36" aria-hidden="true">
      <path d="M24 3A15 15 0 1 0 33 26A12 12 0 0 1 24 3Z" fill="#fff4c2"/>
    </svg>
    <h3>PM STACK</h3>
    <p>Deep Rest<br>Ignite PM<br>EFA</p>
  </section>
</main>
</body>
</html>
```